A clean crisp business card for a Landscape Construction company. Designed to be easy to read contact/ info and also be appealing/interesting, unlike a traditional business card.

Industry/Entity Type

Landscape Construction

Contact Information for Business Card

Company name : Brambleway Landscape Construction, phone number: (877) 61Vista, website:Bramblewaylandscapes.example, Email, sales@bramblewaylandscapes.example

Requirements
Nice to have
• Luxurious finishes/ details…. Icons or emblems next to contact info
Should not have
• Clipart or general pictures

```html
<!DOCTYPE html>
<html lang="en">
<head>
<meta charset="utf-8">
<title>Brambleway Landscape Construction – Business Card</title>
<link rel="stylesheet" href="https://fonts.googleapis.com/css2?family=Cinzel:wght@600&family=Open+Sans:wght@400&display=swap">
<style>
  :root {
    --backdrop: #2b2b2b;
    --card: #242424;
    --card-front: #262626;
    --blue: #2f7ad1;
    --green: #9fd13a;
    --ink: #f2f2f2;
    --emboss: #3a3a3a;
  }
  * { box-sizing: border-box; margin: 0; padding: 0; }
  html, body { width: 1200px; height: 900px; overflow: hidden; }
  body {
    background: var(--backdrop);
    display: flex;
    flex-direction: column;
    align-items: center;
    justify-content: center;
    gap: 36px;
    font-family: "Open Sans", sans-serif;
  }
  .card {
    width: 700px;
    height: 400px;
    position: relative;
    overflow: hidden;
  }
  .card-front {
    background: var(--card-front);
    display: flex;
    align-items: center;
    justify-content: center;
  }
  .front-wordmark {
    font-family: "Cinzel", serif;
    font-weight: 600;
    font-size: 40px;
    letter-spacing: 2px;
    color: var(--emboss);
    text-align: center;
    line-height: 1.25;
  }
  .card-back {
    background: var(--card);
    display: flex;
    align-items: center;
    padding: 0 40px 30px 40px;
  }
  .brand {
    width: 300px;
    display: flex;
    align-items: center;
    gap: 14px;
  }
  .brand-dot {
    width: 22px; height: 22px;
    border-radius: 50%;
    background: var(--blue);
    flex: none;
  }
  .brand-name {
    font-family: "Cinzel", serif;
    font-weight: 600;
    font-size: 27px;
    line-height: 1.25;
    color: var(--green);
  }
  .divider {
    width: 4px;
    height: 200px;
    margin: 0 30px 0 20px;
    display: flex;
    flex-direction: column;
    align-items: center;
  }
  .divider .seg-green { width: 2px; height: 34px; background: var(--green); }
  .divider .seg-blue { width: 4px; flex: 1; background: var(--blue); margin: 6px 0; }
  .contact { color: var(--ink); font-size: 15px; line-height: 1.55; }
  .person-name {
    font-family: "Cinzel", serif;
    font-weight: 600;
    font-size: 26px;
    letter-spacing: 2px;
    line-height: 1.1;
  }
  .person-name .first { color: var(--blue); }
  .person-name .last { color: var(--green); }
  .person-role { font-size: 15px; margin-bottom: 10px; }
  .address { margin-bottom: 8px; }
  .contact-line { display: flex; align-items: center; gap: 10px; }
  .contact-line svg { width: 17px; height: 17px; flex: none; fill: var(--green); }
  .stripe {
    position: absolute; left: 0; right: 0; bottom: 0;
  }
  .stripe-blue { height: 4px; background: var(--blue); bottom: 14px; }
  .stripe-green { height: 14px; background: var(--green); }
</style>
</head>
<body>
  <section class="card card-front" aria-label="Card front">
    <div class="front-wordmark">Brambleway<br>Landscape Construction</div>
  </section>

  <section class="card card-back" aria-label="Card back">
    <div class="brand">
      <span class="brand-dot"></span>
      <span class="brand-name">Brambleway Landscape Construction</span>
    </div>
    <div class="divider">
      <span class="seg-green"></span>
      <span class="seg-blue"></span>
      <span class="seg-green"></span>
    </div>
    <div class="contact">
      <div class="person-name"><span class="first">Mara</span> <span class="last">Ellison</span></div>
      <div class="person-role">Director</div>
      <div class="address">4170 Alder Hollow Rd.,<br>Suite 12, Fernbrook, OH 45999</div>
      <div class="contact-line">
        <svg viewBox="0 0 24 24" aria-hidden="true"><path d="M6.6 10.8a15.1 15.1 0 0 0 6.6 6.6l2.2-2.2a1 1 0 0 1 1-.25 11.4 11.4 0 0 0 3.6.57 1 1 0 0 1 1 1V20a1 1 0 0 1-1 1A17 17 0 0 1 3 4a1 1 0 0 1 1-1h3.5a1 1 0 0 1 1 1c0 1.25.2 2.45.57 3.57a1 1 0 0 1-.25 1z"/></svg>
        <span>(877) 61Vista</span>
      </div>
      <div class="contact-line">
        <svg viewBox="0 0 24 24" aria-hidden="true"><path d="M2 5h20v14H2z" fill="none"/><path d="M2 5h20v2l-10 6L2 7zM2 9l10 6 10-6v10H2z"/></svg>
        <span>sales@bramblewaylandscapes.example</span>
      </div>
      <div class="contact-line">
        <svg viewBox="0 0 24 24" aria-hidden="true"><circle cx="12" cy="12" r="10"/></svg>
        <span>www.bramblewaylandscapes.example</span>
      </div>
    </div>
    <div class="stripe stripe-blue"></div>
    <div class="stripe stripe-green"></div>
  </section>
</body>
</html>
```